International business needs business cards

Our company, DOR Ventures Inc. is in the business of supplying a range construction products with particular emphasis on CEMENT. We have developed our own brand - BRUNVALE MATERIALS - with which to infiltrate the market. We are launching our brand of cement (BRUNVALE Type IS Cement) into the Caribbean which is unlike anything this market has ever seen. A monopoly has existed here for the past 60-odd years and the market has now opened to allow the importation of other brands and consumers are anxious and ready for change/improvement. We are very excited to be launching and want to make a great first impression. We will be conducting workshops and seminars (from government level to the hardware store owners) and we want our business card to give us the strong, confident introduction that we need.

Target Market(s)

construction; builders; engineers; home owners

Industry/Entity Type

Construction

Contact Information for Business Card

Marisol Penwick
CEO
cell # 1 555 4817730
Ground floor,Lantern Plaza Suite 2483
George Town,Grand Cayman
Cayman Islands,KY1-2250
EMAIL: m.penwick@dorventuresinc.example
web site dorventuresinc.example

COMPANY: skype info dor.ventures.example

second card
Tamsin Rowe-Penwick
CFO
CELL# 1 555 604 3917
George Town,Grand Cayman
Cayman Islands,KY1-2250
EMAIL: t.rowepenwick@dorventuresinc.example
website dorventuresinc.example

Requirements
Must have
• Business cards must display BOTH logos - DOR is the company and BRUNVALE is the brand.

```html
<!DOCTYPE html>
<html lang="en">
<head>
<meta charset="utf-8">
<title>DOR Ventures Inc. – Business Card</title>
<link href="https://fonts.googleapis.com/css2?family=Open+Sans:wght@400;600;700&display=swap" rel="stylesheet">
<style>
  :root {
    --backdrop: #e6e3de;
    --card-black: #0b0b0b;
    --card-white: #ffffff;
    --brand-red: #8e2a2a;
    --text-light: #f2f2f2;
    --text-muted: #c9c9c9;
    --text-dark: #151515;
    --brand-grey: #6b6b6b;
  }
  * { box-sizing: border-box; margin: 0; padding: 0; }
  html, body { width: 1200px; height: 843px; overflow: hidden; }
  body {
    background: var(--backdrop);
    font-family: "Open Sans", Arial, sans-serif;
    position: relative;
  }
  .card {
    position: absolute;
    width: 560px;
    height: 320px;
    left: 320px;
    border-radius: 4px;
    box-shadow: 0 8px 24px rgba(0,0,0,.25);
    overflow: hidden;
  }
  /* back side */
  .card-back {
    top: 60px;
    background: linear-gradient(160deg, #1c1c1c 0%, var(--card-black) 45%);
  }
  .card-back .back-mark {
    position: absolute;
    top: 110px; left: 0; right: 0;
    display: flex; align-items: center; justify-content: center; gap: 14px;
  }
  .mark-square {
    width: 46px; height: 46px;
    background: var(--brand-red);
    display: block;
  }
  .back-mark .company-name {
    color: var(--text-light);
    font-size: 34px;
    font-weight: 700;
    letter-spacing: .5px;
  }
  .card-back .back-web {
    position: absolute;
    left: 28px; bottom: 26px;
    color: var(--text-muted);
    font-size: 14px;
    letter-spacing: 1px;
  }
  /* front side */
  .card-front {
    top: 450px;
    display: flex;
    background: var(--card-black);
  }
  .front-identity {
    width: 290px;
    background: var(--card-white);
    border-right: 3px solid var(--brand-red);
    padding: 34px 24px 24px 30px;
    display: flex; flex-direction: column; align-items: flex-start;
  }
  .company-lockup {
    display: flex; align-items: center; gap: 10px;
  }
  .company-lockup .mark-square { width: 40px; height: 40px; }
  .company-lockup .company-name {
    color: var(--text-dark);
    font-size: 24px;
    font-weight: 700;
  }
  .brand-lockup {
    margin-top: 46px;
    margin-left: 20px;
    display: flex; align-items: center; gap: 10px;
  }
  .brand-dot {
    width: 30px; height: 30px; border-radius: 50%;
    background: var(--brand-grey);
  }
  .brand-lockup .brand-name {
    color: var(--brand-grey);
    font-size: 20px;
    font-weight: 700;
    letter-spacing: 1px;
  }
  .front-contact {
    flex: 1;
    padding: 30px 22px 20px 26px;
    color: var(--text-light);
    border-left: 2px solid #2a2a2a;
  }
  .person-name { font-size: 20px; font-weight: 600; }
  .person-role { font-size: 13px; color: var(--text-muted); margin-bottom: 22px; }
  .address { font-size: 14px; line-height: 1.35; margin-bottom: 8px; }
  .contact-line {
    display: flex; align-items: center; gap: 10px;
    font-size: 14px; line-height: 1.55;
  }
  .contact-line svg { width: 13px; height: 13px; flex: none; }
</style>
</head>
<body>

<section class="card card-back" aria-label="Card back">
  <div class="back-mark">
    <span class="mark-square"></span>
    <span class="company-name">DOR Ventures Inc.</span>
  </div>
  <div class="back-web">www.dorventuresinc.example</div>
</section>

<section class="card card-front" aria-label="Card front">
  <div class="front-identity">
    <div class="company-lockup">
      <span class="mark-square"></span>
      <span class="company-name">DOR Ventures Inc.</span>
    </div>
    <div class="brand-lockup">
      <span class="brand-dot"></span>
      <span class="brand-name">BRUNVALE</span>
    </div>
  </div>

  <div class="front-contact">
    <div class="person-name">Marisol Penwick</div>
    <div class="person-role">CEO</div>
    <div class="address">
      Ground floor<br>
      Lantern Plaza Suite 2483<br>
      George Town,Grand Cayman<br>
      Cayman Islands,KY1-2250
    </div>
    <div class="contact-line">
      <svg viewBox="0 0 12 12" aria-hidden="true"><rect x="3" y="0.5" width="6" height="11" rx="1" fill="none" stroke="#f2f2f2"/><circle cx="6" cy="9.5" r=".7" fill="#f2f2f2"/></svg>
      <span>1 555 4817730</span>
    </div>
    <div class="contact-line">
      <svg viewBox="0 0 12 12" aria-hidden="true"><rect x=".5" y="2" width="11" height="8" fill="none" stroke="#f2f2f2"/><path d="M.5 2 6 6.5 11.5 2" fill="none" stroke="#f2f2f2"/></svg>
      <span>m.penwick@dorventuresinc.example</span>
    </div>
    <div class="contact-line">
      <svg viewBox="0 0 12 12" aria-hidden="true"><circle cx="6" cy="6" r="5.5" fill="#f2f2f2"/><path d="M.5 6h11M6 .5c-2.5 3-2.5 8 0 11M6 .5c2.5 3 2.5 8 0 11" fill="none" stroke="#0b0b0b" stroke-width=".8"/></svg>
      <span>www.dorventuresinc.example</span>
    </div>
  </div>
</section>

</body>
</html>
```